New Television Homescreen Template

We need a new default homescreen design for our televisions. This should reflect our company branding. My company is called Wardline Systems, WLS for short. Our website is www.wlsx.example. We develop televisions and infotainment solutions for the healthcare industry. I am somewhat open to different color palettes but our company colors are blue, black, and white. Our design is constrained by the 9 buttons, however the design of the buttons can be changed. Also, there is a video box on the right side of the screen as shown, this design can also be changed.

Target Market(s)

Hospital Patients

Requirements
Must have
• PSD template.

```html
<!DOCTYPE html>
<html lang="en">
<head>
<meta charset="utf-8">
<title>Wardline Systems – Patient Homescreen</title>
<link rel="stylesheet" href="https://fonts.googleapis.com/css2?family=Quicksand:wght@300;400&family=Roboto+Condensed:wght@700&family=Roboto:wght@400;700&display=swap">
<style>
  :root {
    --ink-white: #ffffff;
    --night: #0c1c26;
    --night-mid: #163742;
    --harbor: #1f6f6c;
    --accent-sky: #7fd3f2;
    --accent-blue: #3aa9e0;
    --accent-soft: #b9e6f7;
    --player-bg: #1d242c;
    --player-art: #3a4450;
    --play-face: #e9ecef;
    --play-arrow: #1f8fb0;
    --brand-dark: #1a1f24;
    --brand-muted: #4a5660;
    --tile-welcome: #a81e2a;
    --tile-cable: #a7b841;
    --tile-movies: #ad8f2b;
    --tile-map: #2ebf36;
    --tile-portal: #2279d4;
    --tile-dining: #8a25ad;
    --tile-phone: #cf2f82;
    --tile-education: #37a6a7;
    --tile-request: #1f2e2b;
  }
  html, body {
    margin: 0;
    padding: 0;
    width: 1200px;
    height: 675px;
    overflow: hidden;
    background: var(--night);
  }
  .homescreen {
    position: relative;
    width: 1200px;
    height: 675px;
    overflow: hidden;
    font-family: "Quicksand", sans-serif;
  }
  .backdrop {
    position: absolute;
    inset: 0;
    background:
      radial-gradient(circle 26px at 193px 76px, rgba(140,240,220,0.75), rgba(140,240,220,0.2) 70%, transparent 100%),
      radial-gradient(ellipse 420px 160px at 900px 560px, rgba(83,216,194,0.55), transparent 70%),
      radial-gradient(ellipse 500px 180px at 300px 400px, rgba(40,140,120,0.45), transparent 70%),
      linear-gradient(180deg, var(--night) 0%, var(--night-mid) 38%, var(--harbor) 68%, #2d8f86 100%);
  }
  .glow-band {
    position: absolute;
    left: 0;
    top: 515px;
    width: 1200px;
    height: 160px;
    background:
      radial-gradient(ellipse 420px 140px at 300px 40px, rgba(255,255,255,0.98), rgba(255,255,255,0.75) 55%, transparent 100%),
      linear-gradient(180deg, rgba(255,255,255,0.85) 0%, rgba(255,255,255,0.55) 50%, rgba(255,255,255,0.25) 100%);
    -webkit-mask-image: linear-gradient(90deg, #000 0%, #000 45%, rgba(0,0,0,0.25) 75%, transparent 100%);
    mask-image: linear-gradient(90deg, #000 0%, #000 45%, rgba(0,0,0,0.25) 75%, transparent 100%);
  }
  .mission {
    position: absolute;
    left: 110px;
    top: 100px;
    width: 380px;
    margin: 0;
    text-align: center;
    font-weight: 300;
    color: var(--ink-white);
    line-height: 1;
  }
  .mission-line { display: block; white-space: nowrap; height: 33px; }
  .mission-small { font-size: 20px; color: var(--accent-soft); }
  .mission-mid { font-size: 30px; }
  .mission-large { font-size: 40px; color: var(--accent-sky); }
  .mission-blue { color: var(--accent-blue); }

  .video-player {
    position: absolute;
    left: 92px;
    top: 277px;
    width: 423px;
    height: 238px;
    background: var(--player-bg);
  }
  .video-art {
    position: absolute;
    left: 90px;
    top: 10px;
    width: 243px;
    height: 228px;
    background: radial-gradient(ellipse at 50% 40%, var(--player-art), var(--player-bg) 70%);
  }
  .play-button {
    position: absolute;
    left: 173px;
    top: 110px;
    width: 60px;
    height: 43px;
  }
  .brand {
    position: absolute;
    left: 162px;
    top: 540px;
    width: 300px;
  }
  .brand-name {
    font-size: 28px;
    font-weight: 400;
    color: var(--brand-dark);
    white-space: nowrap;
  }
  .brand-line {
    font-family: "Roboto", sans-serif;
    font-weight: 400;
    font-size: 11px;
    color: var(--brand-muted);
    margin-top: 3px;
    letter-spacing: 0.4px;
  }
  .menu-grid {
    position: absolute;
    left: 652px;
    top: 203px;
    display: grid;
    grid-template-columns: repeat(3, 137px);
    grid-template-rows: repeat(3, 90px);
    column-gap: 10px;
    row-gap: 17px;
  }
  .menu-tile {
    position: relative;
    display: flex;
    align-items: center;
    justify-content: center;
    text-align: center;
    border-radius: 3px;
    color: var(--ink-white);
    font-family: "Roboto", sans-serif;
    font-weight: 700;
    font-size: 18px;
    line-height: 0.98;
    text-transform: uppercase;
    box-shadow: 0 1px 3px rgba(0,0,0,0.25);
    overflow: hidden;
  }
  .menu-tile::after {
    content: "";
    position: absolute;
    inset: 0;
    background: linear-gradient(160deg, rgba(255,255,255,0.12), rgba(255,255,255,0) 55%, rgba(0,0,0,0.08));
  }
  .menu-tile.is-small { font-size: 15.5px; }
  .menu-tile.is-welcome {
    font-family: "Roboto Condensed", sans-serif;
    font-size: 27px;
    letter-spacing: -0.5px;
  }
  .tile-welcome { background: var(--tile-welcome); }
  .tile-cable { background: var(--tile-cable); }
  .tile-movies { background: var(--tile-movies); }
  .tile-map { background: var(--tile-map); }
  .tile-portal { background: var(--tile-portal); }
  .tile-dining { background: var(--tile-dining); }
  .tile-phone { background: var(--tile-phone); }
  .tile-education { background: var(--tile-education); opacity: 0.92; }
  .tile-request { background: linear-gradient(180deg, var(--tile-request), #3e4f4b); }
</style>
</head>
<body>
<main class="homescreen">
  <div class="backdrop" role="img" aria-label="Blurred night view of a lit suspension bridge over city water"></div>
  <div class="glow-band"></div>

  <h1 class="mission">
    <span class="mission-line"><span class="mission-small">Rest easy,</span> <span class="mission-mid">stay close</span></span>
    <span class="mission-line"><span class="mission-small">to the</span> <span class="mission-large">people you love</span></span>
    <span class="mission-line"><span class="mission-mid">from your</span> <span class="mission-mid mission-blue">bedside</span></span>
  </h1>

  <section class="video-player" aria-label="Welcome video">
    <div class="video-art" role="img" aria-label="Soft white illustration of a tree with leaves"></div>
    <svg class="play-button" viewBox="0 0 60 43" aria-label="Play">
      <rect x="0" y="0" width="60" height="43" rx="4" fill="var(--play-face)"/>
      <polygon points="24,12 24,31 40,21.5" fill="var(--play-arrow)"/>
    </svg>
  </section>

  <div class="brand">
    <div class="brand-name">Wardline Systems</div>
    <div class="brand-line">www.wlsx.example</div>
  </div>

  <nav class="menu-grid">
    <div class="menu-tile is-welcome tile-welcome">Welcome</div>
    <div class="menu-tile tile-cable">Cable TV</div>
    <div class="menu-tile tile-movies">Movies</div>
    <div class="menu-tile tile-map">Campus<br>Map</div>
    <div class="menu-tile tile-portal">Northgate<br>Portal</div>
    <div class="menu-tile tile-dining">Dining<br>Options</div>
    <div class="menu-tile is-small tile-phone">Important<br>Phone<br>Numbers</div>
    <div class="menu-tile is-small tile-education">Patient<br>Education<br>Materials</div>
    <div class="menu-tile tile-request">Request<br>Services</div>
  </nav>
</main>
</body>
</html>
```